Business Card Design

This is a new business to be run from my home. I have attended certificate workshops run by Dr Derek Onwu who is a Master Trainer in Harbor Steps Method.
I wish to communicate to people that Tai Chi is for everyone, no matter their age, gender or fitness levels. Tai Chi is taught both standing & seated.
The card should have a slightly Asian feel, mainly printed in black & white with perhaps a little soft pink &/or green.

Target Market(s)

people of all ages from 10 years up, poor fitness & mild disabilities.

Industry/Entity Type

Fitness

Contact Information for Business Card

Wexmoor Tai Chi for Fitness, Health & Relaxation

Branna Holt, Certificated Leader

ph 4091 5528

Requirements
Nice to have
• a feeling of health & peace.
Should not have
• bright colours, fancy fonts

```html
<!DOCTYPE html>
<html lang="en">
<head>
<meta charset="utf-8">
<title>Wexmoor Tai Chi for Fitness – Business Card</title>
<link rel="stylesheet" href="https://fonts.googleapis.com/css2?family=Archivo+Black&family=Montserrat:wght@400;500&display=swap">
<style>
  :root {
    --page-bg: #f2f2f2;
    --card-black: #0b0b0b;
    --card-charcoal: #1c1c1c;
    --leaf-green: #3ed44a;
    --line-green: #2f8a34;
    --silver-light: #f4f4f4;
    --silver-mid: #b9b9b9;
    --silver-dark: #7a7a7a;
    --text-white: #f5f5f5;
    --art-light: #dcdcdc;
    --art-mid: #8e8e8e;
    --art-dark: #3a3a3a;
  }
  * { margin: 0; padding: 0; box-sizing: border-box; }
  html, body {
    width: 1200px; height: 900px; overflow: hidden;
    background: var(--page-bg);
  }
  .card {
    position: absolute; left: 100px; top: 165px;
    width: 1000px; height: 570px;
    border-radius: 42px; overflow: hidden;
    background:
      radial-gradient(ellipse 45% 35% at 50% 42%, rgba(255,255,255,0.09), transparent 70%),
      repeating-linear-gradient(45deg, rgba(255,255,255,0.025) 0 2px, transparent 2px 5px),
      linear-gradient(180deg, var(--card-charcoal), var(--card-black) 60%);
    box-shadow: 0 14px 40px rgba(0,0,0,0.25);
  }
  .business-name {
    position: absolute; top: 96px; left: 0; width: 100%;
    text-align: center;
    font-family: "Archivo Black", sans-serif;
    font-size: 46px; line-height: 1; letter-spacing: 0.01em;
    background: linear-gradient(180deg, var(--silver-light) 0%, var(--silver-mid) 50%, var(--silver-dark) 52%, var(--silver-light) 100%);
    -webkit-background-clip: text; background-clip: text;
    color: transparent;
  }
  .tagline {
    position: absolute; top: 156px; left: 0; width: 100%;
    text-align: center; padding-left: 0.68em;
    font-family: "Montserrat", sans-serif; font-weight: 500;
    font-size: 27px; line-height: 1; letter-spacing: 0.68em;
    color: var(--leaf-green);
  }
  .divider {
    position: absolute; top: 292px; left: 0; width: 100%; height: 3px;
    background: linear-gradient(90deg, rgba(47,138,52,0.3), var(--line-green) 30%, var(--leaf-green) 60%, rgba(47,138,52,0.2));
  }
  .divider-lower {
    position: absolute; top: 500px; left: 0; width: 100%; height: 2px;
    background: linear-gradient(90deg, transparent, rgba(47,138,52,0.5) 40%, transparent);
  }
  .leader-name {
    position: absolute; top: 334px; left: 80px;
    font-family: "Montserrat", sans-serif; font-weight: 500;
    font-size: 42px; line-height: 1; color: var(--leaf-green);
  }
  .leader-role {
    position: absolute; top: 385px; left: 80px;
    font-family: "Montserrat", sans-serif; font-weight: 400;
    font-size: 29px; line-height: 1; color: var(--text-white);
  }
  .phone {
    position: absolute; top: 446px; left: 80px;
    display: flex; align-items: center; gap: 14px;
    font-family: "Montserrat", sans-serif; font-weight: 500;
    font-size: 40px; line-height: 1; color: var(--text-white);
  }
  .phone svg { width: 36px; height: 36px; fill: var(--leaf-green); }
  .figure-art {
    position: absolute; left: 700px; top: 200px;
    width: 270px; height: 270px; border-radius: 24px;
    background: linear-gradient(160deg, var(--art-light) 0%, var(--art-mid) 55%, var(--art-dark) 100%);
    box-shadow: 0 8px 24px rgba(0,0,0,0.5);
  }
</style>
</head>
<body>
  <div class="card">
    <div class="business-name">WEXMOOR TAI CHI FOR FITNESS</div>
    <div class="tagline">Health &amp; Relaxation</div>
    <div class="divider"></div>
    <div class="divider-lower"></div>
    <div class="figure-art" role="img" aria-label="Illustration of a tai chi practitioner in white clothing in a low stance on a round black and white disc"></div>
    <div class="leader-name">Branna Holt</div>
    <div class="leader-role">Certificated Leader</div>
    <div class="phone">
      <svg viewBox="0 0 24 24" aria-hidden="true"><path d="M6.6 10.8a15.1 15.1 0 0 0 6.6 6.6l2.2-2.2a1 1 0 0 1 1-.25 11.4 11.4 0 0 0 3.6.57 1 1 0 0 1 1 1V20a1 1 0 0 1-1 1A17 17 0 0 1 3 4a1 1 0 0 1 1-1h3.5a1 1 0 0 1 1 1c0 1.25.2 2.45.57 3.6a1 1 0 0 1-.25 1z"/></svg>
      <span>4091 5528</span>
    </div>
  </div>
</body>
</html>
```